Drowsy Heron

Need a business card for our restaurant. Restaurant and Bar in the mountains of North Idaho. Rustic looking card

Contact Information for Business Card

rustic design, wood and metal looking, primarily neutral colors

Requirements
Must have
• Name, address, phone number, website, email address

```html
<!DOCTYPE html>
<html lang="en">
<head>
<meta charset="utf-8">
<title>Drowsy Heron – Business Card</title>
<link rel="stylesheet" href="https://fonts.googleapis.com/css2?family=Montserrat:wght@400;600&display=swap">
<style>
  :root {
    --page-bg: #d4ccc1;
    --frost: #e9e1d4;
    --badge: #dccfbb;
    --panel: #1d1b19;
    --panel-edge: #2a2724;
    --ink-light: #d9cdb9;
    --ink-soft: #c9bda9;
    --ink-dark: #1d1b19;
    --rule: #b9ad9a;
  }
  * { margin: 0; padding: 0; box-sizing: border-box; }
  html, body {
    width: 1047px;
    height: 1200px;
    overflow: hidden;
    background: var(--page-bg);
    font-family: "Montserrat", sans-serif;
  }
  .card {
    position: absolute;
    left: 243px;
    top: 88px;
    width: 560px;
    height: 1025px;
    border-radius: 22px;
    overflow: hidden;
    background: var(--frost);
    box-shadow: 0 18px 40px rgba(60, 45, 30, 0.18);
  }
  .card__panel {
    position: absolute;
    left: 0;
    top: 260px;
    width: 100%;
    height: 765px;
    background: linear-gradient(180deg, var(--panel-edge) 0%, var(--panel) 35%, var(--panel) 100%);
  }
  .card__badge {
    position: absolute;
    left: 87px;
    top: 53px;
    width: 386px;
    height: 386px;
    border-radius: 50%;
    background: var(--badge);
    display: flex;
    align-items: center;
    justify-content: center;
  }
  .brand-name {
    font-weight: 600;
    font-size: 38px;
    color: var(--ink-dark);
    letter-spacing: 0.04em;
    text-transform: uppercase;
    text-align: center;
    line-height: 1.2;
  }
  .person {
    position: absolute;
    left: 0;
    width: 100%;
    text-align: center;
  }
  .person__name {
    top: 512px;
    font-weight: 600;
    font-size: 40px;
    color: var(--ink-light);
  }
  .person__title {
    top: 570px;
    font-weight: 400;
    font-size: 25px;
    color: var(--ink-soft);
  }
  .contact-icons {
    position: absolute;
    top: 648px;
    left: 0;
    width: 100%;
    display: flex;
    align-items: center;
    justify-content: center;
    gap: 10px;
  }
  .contact-icons__rule {
    width: 90px;
    height: 2px;
    background: var(--rule);
    margin: 0 6px;
  }
  .contact-icons svg { width: 38px; height: 38px; display: block; }
  .contact-list {
    position: absolute;
    top: 718px;
    left: 0;
    width: 100%;
    list-style: none;
    text-align: center;
    font-size: 25px;
    line-height: 42px;
    color: var(--ink-light);
  }
  .contact-divider {
    position: absolute;
    top: 855px;
    left: 133px;
    width: 294px;
    height: 2px;
    background: var(--rule);
  }
  .address {
    position: absolute;
    top: 872px;
    left: 0;
    width: 100%;
    text-align: center;
    font-style: normal;
    font-size: 25px;
    line-height: 42px;
    color: var(--ink-soft);
  }
</style>
</head>
<body>
  <div class="card">
    <div class="card__panel"></div>
    <div class="card__badge">
      <p class="brand-name">Drowsy<br>Heron</p>
    </div>

    <p class="person person__name">Owen Hartley</p>
    <p class="person person__title">Managing Director</p>

    <div class="contact-icons">
      <span class="contact-icons__rule"></span>
      <svg viewBox="0 0 38 38" aria-label="Phone">
        <rect width="38" height="38" rx="8" fill="var(--badge)"/>
        <path d="M10 15c0-3 4-5 9-5s9 2 9 5v2h-5v-2h-8v2h-5z" fill="var(--ink-dark)"/>
        <path d="M12 19h14l2 9H10z" fill="var(--ink-dark)"/>
        <circle cx="19" cy="23.5" r="2.5" fill="var(--badge)"/>
      </svg>
      <svg viewBox="0 0 38 38" aria-label="Email">
        <rect width="38" height="38" rx="8" fill="var(--badge)"/>
        <rect x="8" y="11" width="22" height="16" rx="2" fill="var(--ink-dark)"/>
        <path d="M9 12l10 8 10-8" fill="none" stroke="var(--badge)" stroke-width="2"/>
      </svg>
      <svg viewBox="0 0 38 38" aria-label="Website">
        <rect width="38" height="38" rx="8" fill="var(--badge)"/>
        <circle cx="19" cy="19" r="10" fill="var(--ink-dark)"/>
        <ellipse cx="19" cy="19" rx="4" ry="10" fill="none" stroke="var(--badge)" stroke-width="1.5"/>
        <path d="M9 19h20M11 14h16M11 24h16" stroke="var(--badge)" stroke-width="1.5"/>
      </svg>
      <span class="contact-icons__rule"></span>
    </div>

    <ul class="contact-list">
      <li>123 456 789</li>
      <li>info@yourmail.com</li>
      <li>www.yourwebsite.com</li>
    </ul>

    <div class="contact-divider"></div>

    <address class="address">
      Your address, City<br>
      State, Zip 1234
    </address>
  </div>
</body>
</html>
```